Tender / Request for Quotation response template

KELTRA58 is a small consulting company that works in management consulting with a particular emphasis on tourism, sport, major events and general commercial. our clients range from government , councils, private businesses and industry associations.

we are regularly asked to submit detailed quotes or tender responses and we use our own PowerPoint template to do so as we find it its generally easier to work with.

our website provides more detail : www.keltra58.com.au the colour of the blue in logo is #000033

our submissions range from 30 pages to 100 pages depending on the size and scale of the project - so we need flexibility with the templates.

Our submissions generally include cover page and table of contents and then
1. Project overview
2. About KELTRA58
3. The project team including bios
4. Initial Insights
5. importance of sustainability
6. Project methodology - example being
6.1 situation analysis
- research
- consultation and engagement
- relevant audits
- relevant economic analysis including graphs
- gap analysis
- SWOT
6.2 Issues and opportunities
6.3 draft report
6.4 final report
7. Case studies and previous relevant work
8. Project timeline
9. Project budget
10. Insurance and referees

we use many graphs and tables from excel and images generally sourced from the web. we also use icons as appropriate so we need graph templates - column, bar / pie etc and table templates.

the feel is on the formal corporate side given the size and scale of projects and clients but with bright and clear graphics and photos.

i have attached 2 copies of confidential submissions that we have made in recent weeks. one long form and one short form to give you an idea of the flexibility we need in the submission process.

if we are happy with the proposed PowerPoint tender submission template we would then look to have a similar one created to use in the development of the actual reports themselves .

hopefully this provides enough information but if not please reach out for more information

our logo and general format are in the attached examples

Target Market(s)

government, council, corporates and private businesses

Industry/Entity Type

management consulting with emphasis on tourism sport major events nd general commerical

• we usually use calbiri but open to other standard microsoft off the shelf fonts

Colors
0054AA
0677BA
7BADD7
CADEEF
E8F1F8
0094D4
00A9DD
6FCCEA
C7EBF8
E9F6FB

Requirements
Must have
• page for each of the sections detailed in the project brief. image placement - small and large, table and graph formats,

```html
<!DOCTYPE html>
<html lang="en">
<head>
<meta charset="utf-8">
<title>KELTRA58 Project Team</title>
<link href="https://fonts.googleapis.com/css2?family=Barlow+Condensed:wght@600&family=Carlito:wght@400;700&display=swap" rel="stylesheet">
<style>
  :root {
    --blue-deep: #0049a0;
    --blue-main: #0054AA;
    --blue-mid: #0677BA;
    --blue-light: #7BADD7;
    --panel: #0a4d9f;
    --white: #ffffff;
    --photo-warm: #b9a58f;
    --photo-cool: #c9d3da;
  }
  * { margin: 0; padding: 0; box-sizing: border-box; }
  html, body { width: 1200px; height: 655px; overflow: hidden; }
  body { background: var(--blue-main); }
  .slide {
    position: relative;
    width: 1200px;
    height: 655px;
    overflow: hidden;
    color: var(--white);
    font-family: "Carlito", "Calibri", sans-serif;
    background:
      radial-gradient(ellipse 620px 180px at 900px 640px, rgba(10,70,160,0.9), transparent 70%),
      radial-gradient(ellipse 900px 500px at 1150px 200px, rgba(0,95,190,0.6), transparent 70%),
      linear-gradient(160deg, #0056b0 0%, var(--blue-main) 45%, var(--blue-deep) 100%);
  }
  .slide-swoosh { position: absolute; inset: 0; }
  .slide-title {
    position: absolute;
    left: 38px; top: 50px;
    font-family: "Barlow Condensed", "Arial Narrow", sans-serif;
    font-weight: 600;
    font-size: 44px;
    letter-spacing: -1px;
  }
  .portrait {
    position: absolute;
    width: 102px; height: 102px;
    border-radius: 50%;
    background: radial-gradient(circle at 50% 40%, var(--photo-warm), var(--photo-cool));
    box-shadow: 0 3px 6px rgba(0,0,0,0.35);
  }
  .member-name {
    font-family: "Barlow Condensed", "Arial Narrow", sans-serif;
    font-weight: 600;
    font-size: 26px;
    letter-spacing: -0.6px;
    line-height: 1;
  }
  .member-role { font-size: 18px; line-height: 1.25; margin-top: 3px; }
  .member { position: absolute; left: 164px; }
  .advisor { position: absolute; left: 655px; top: 164px; }
  .advisor-bio {
    position: absolute;
    left: 647px; top: 212px;
    width: 379px; height: 313px;
    background: var(--panel);
    box-shadow: 0 3px 8px rgba(0,0,0,0.35);
    padding: 11px 6px 0 4px;
    font-size: 13.6px;
    line-height: 18px;
    white-space: nowrap;
    overflow: hidden;
  }
  .advisor-bio p { margin-bottom: 8.5px; }
  .advisor-bio p span { padding-left: 3px; }
  .partner-heading {
    position: absolute;
    left: 37px; top: 512px;
    font-family: "Barlow Condensed", "Arial Narrow", sans-serif;
    font-weight: 600;
    font-size: 20px;
    letter-spacing: -0.4px;
  }
  .partner-mark {
    position: absolute;
    left: 239px; top: 548px;
    display: flex; align-items: center; gap: 10px;
  }
  .partner-mark .square { width: 40px; height: 40px; background: var(--blue-light); }
  .partner-mark .name { font-size: 30px; font-weight: 700; color: var(--white); }
</style>
</head>
<body>
<main class="slide">
  <svg class="slide-swoosh" width="1200" height="655" viewBox="0 0 1200 655" aria-hidden="true">
    <path d="M0 560 C 300 470, 700 520, 1200 600 L1200 655 L0 655 Z" fill="#0050a8" opacity="0.55"/>
    <path d="M300 655 C 600 560, 900 560, 1200 520 L1200 655 Z" fill="#004a9e" opacity="0.5"/>
  </svg>

  <h1 class="slide-title">KELTRA58 PROJECT TEAM</h1>

  <div class="portrait" style="left:51px; top:144px;" role="img" aria-label="Portrait photo of Daniel Harrow"></div>
  <div class="member" style="top:170px;">
    <div class="member-name">DANIEL HARROW</div>
    <div class="member-role">Project Leader, Strategic Planning, Analysis</div>
  </div>

  <div class="portrait" style="left:51px; top:259px;" role="img" aria-label="Portrait photo of Owen Prescott"></div>
  <div class="member" style="top:279px;">
    <div class="member-name">OWEN PRESCOTT</div>
    <div class="member-role">&nbsp;Project Manager Strategic Planning,<br>&nbsp;&nbsp;Stakeholder Engagement, Research</div>
  </div>

  <div class="portrait" style="left:51px; top:371px;" role="img" aria-label="Portrait photo of Marcus Delaney"></div>
  <div class="member" style="top:396px;">
    <div class="member-name">MARCUS DELANEY</div>
    <div class="member-role">Economic Analysis, Investment Attraction</div>
  </div>

  <div class="portrait" style="left:547px; top:138px;" role="img" aria-label="Portrait photo of Claire Ashby"></div>
  <div class="advisor">
    <div class="member-name">CLAIRE ASHBY</div>
    <div class="member-role">Project advisor</div>
  </div>

  <div class="advisor-bio">
    <p>KELTRA58's newest team member, brings a wealth of experience<br><span>as an attractions specialist, serving as a general project advisor.</span></p>
    <p>Her extensive career spans both the private and public sectors,<br><span>encompassing tourism, events, marketing, and advertising.</span></p>
    <p>Claire currently advises NOVA Creative Marketing and has held<br><span>CEO positions at Northgate Partners and RTIC in the past.</span></p>
    <p>Prior to that, she served as GM Marketing for the Harbourside<br><span>Aquarium and Reef Discovery World on the Coral Coast.</span></p>
    <p>Additionally, Claire holds the Vice-Chair position at Heritage<br><span>Attractions Network and serves as a non-executive director</span><br><span>for Wildlife Parks Southern.</span></p>
    <p>Her academic background includes a Bachelor of Business<br><span>in Tourism and Information Systems, along with qualifications</span><br><span>from the IBDA.</span></p>
  </div>

  <h2 class="partner-heading">OUR TEAM WILL BE SUPPORTED BY OUR LEADING MARKET RESEARCH PARTNER:</h2>
  <div class="partner-mark">
    <div class="square"></div>
    <div class="name">VANTORA Research</div>
  </div>
</main>
</body>
</html>
```